Chiropody and Podiatry Flyer

A6 Flyer for a Chiropody Clinic.
Need to use an existing company logo (upload available).
Flyer should promote three aspects of the practice;
1) General chiropody : Nail Cutting; Corn Removal; Ingrown Nails; Hard Skin Removal; Verruca Treatment; Diabetic Assessment; Nail Surgery.
2) Home Visits - chiropody in the comfort of your own home.
3) Biomechanical Assessments / Orthotics
Colours should comprise navy blue/green/white to complement existing logo.
Promotional Offer on flyer.

Industry/Entity Type

Clinic

```html
<!DOCTYPE html>
<html lang="en">
<head>
<meta charset="utf-8">
<title>Ember Court for Health – Chiropody Flyer</title>
<link href="https://fonts.googleapis.com/css2?family=Questrial&family=Allura&family=Cinzel:wght@400&display=swap" rel="stylesheet">
<style>
  :root {
    --backdrop: #e8e5e0;
    --card: #ffffff;
    --navy: #0b3f8c;
    --navy-deep: #0a2a5c;
    --ink-band: #0b1a33;
    --green: #4fd13a;
    --white: #ffffff;
    --script: #1c3f86;
    --badge: #2a4f9c;
    --badge-red: #8c2530;
  }
  * { margin: 0; padding: 0; box-sizing: border-box; }
  html, body { width: 1200px; height: 594px; overflow: hidden; background: var(--backdrop); }
  .flyer {
    position: absolute; left: 108px; top: 88px; width: 982px; height: 418px;
    background: var(--card); box-shadow: 0 2px 6px rgba(0,0,0,.15);
  }
  .photo { position: absolute; top: 32px; height: 352px; }
  .photo--runner { left: 32px; width: 152px;
    background: linear-gradient(180deg, #c9cfd6 0%, #8aa0c8 40%, #eef0f3 80%, #ffffff 100%); }
  .photo--yoga { left: 184px; width: 155px;
    background: radial-gradient(circle at 50% 52%, #fff7d6 0%, #e9c98a 18%, #a98f6e 45%, #5c5348 75%, #d8d4cf 100%); }
  .photo--beach { left: 339px; width: 153px;
    background: linear-gradient(180deg, #4fa3a8 0%, #36b7c6 30%, #b88a6c 55%, #e9e3dc 85%, #f5f2ee 100%); }
  .photo__word {
    position: absolute; bottom: 42px; left: 0; right: 0; text-align: center;
    font-family: "Allura", cursive; font-size: 40px; color: var(--script);
  }
  .services {
    position: absolute; left: 492px; top: 32px; width: 458px; height: 175px;
    background: linear-gradient(180deg, var(--navy-deep) 0%, var(--navy) 100%);
    font-family: "Questrial", sans-serif; color: var(--white);
    text-align: center; padding-top: 41px; font-size: 13px; line-height: 21px;
  }
  .services__heading { color: var(--green); font-weight: bold; font-size: 12.5px; letter-spacing: .2px; }
  .brand {
    position: absolute; left: 663px; top: 219px; width: 114px; height: 84px;
    background: var(--navy-deep); display: flex; align-items: center; justify-content: center;
    font-family: "Questrial", sans-serif; color: var(--green); font-size: 13px;
    text-align: center; line-height: 16px;
  }
  .badge { position: absolute; }
  .badge--register { left: 537px; top: 290px; width: 78px; height: 16px; background: var(--badge); }
  .badge--society { left: 826px; top: 280px; width: 26px; height: 26px; background: var(--badge-red); }
  .contact {
    position: absolute; left: 492px; top: 319px; width: 458px; height: 66px;
    background: var(--ink-band); color: var(--white);
    font-family: "Questrial", sans-serif; font-size: 12.5px; font-weight: bold;
    text-align: center; padding-top: 12px; line-height: 20px;
  }
  .contact__phone { display: inline-flex; align-items: center; gap: 4px; margin-left: 8px; }
  .contact__phone svg { width: 12px; height: 12px; }
</style>
</head>
<body>
  <div class="flyer">
    <div class="photo photo--runner" role="img" aria-label="Woman jogging in a blue top along a snowy path">
      <span class="photo__word">Restore</span>
    </div>
    <div class="photo photo--yoga" role="img" aria-label="Woman in a tree yoga pose against the sunlight">
      <span class="photo__word">Renew</span>
    </div>
    <div class="photo photo--beach" role="img" aria-label="Woman in a white dress with a flower in her hair facing a turquoise sea">
      <span class="photo__word">Revitalise</span>
    </div>

    <div class="services">
      <div class="services__heading">1) GENERAL CHIROPODY :</div>
      <div>Nail Cutting | Corn Removal | Ingrown Nails | Hard Skin Removal</div>
      <div>Verruca Treatment | Diabetic Assessment | Nail Surgery.</div>
      <div class="services__heading">2) HOME VISITS</div>
      <div>Chiropody in the comfort of your own home.</div>
      <div class="services__heading">3) BIOMECHANICAL ASSESSMENTS / ORTHOTICS</div>
    </div>

    <div class="brand">Ember Court<br>for Health</div>
    <div class="badge badge--register" role="img" aria-label="Professional registration badge"></div>
    <div class="badge badge--society" role="img" aria-label="Professional society membership badge"></div>

    <div class="contact">
      <div>4B, Kestrel House, Marsh Lane Estate, Mill Road, Greyhaven,</div>
      <div>Essex, CM7 2QT
        <span class="contact__phone"><svg viewBox="0 0 12 12"><circle cx="6" cy="6" r="6" fill="#4fd13a"/><path d="M4 3.2l1 1.2-.6.8a4 4 0 0 0 2.4 2.4l.8-.6 1.2 1-.6.9c-2.4 0-4.9-2.5-4.9-4.9z" fill="#0b1a33"/></svg>07700 900481</span>
        <span class="contact__phone"><svg viewBox="0 0 12 12"><circle cx="6" cy="6" r="6" fill="#4fd13a"/><path d="M4 3.2l1 1.2-.6.8a4 4 0 0 0 2.4 2.4l.8-.6 1.2 1-.6.9c-2.4 0-4.9-2.5-4.9-4.9z" fill="#0b1a33"/></svg>01632 960514</span>
      </div>
    </div>
  </div>
</body>
</html>
```